Avocado Smoothies (100% Natural, No Preservatives, No added Sugar)

We need a company logo (for business cards etc) as well as label design (front and back) for a range of avocado based smoothies on our 300 ml bottle & pouch with drinking spout. The look & feel of the label is that the smoothies are fresh & healthy, prepared with freshest ingredients & formulated with nutritional needs in mind.

The final design should give the impression of a genuine & trusted brand of beverage that is appealing to (1) health conscious busy professionals both male & female (e.g. gym / yoga / athletic buffs), (2) busy mothers of fussy / picky kids; and (3) people who like more plant-based diets, who want the best products for them / their families. The design is to be innovative & appealing to the intelligent health conscious consumers especially avocado fans, looking for healthier alternatives of natural drinks on-the go, that are NOT prepared by big, impersonal & highly automated factories that use all sorts of nasties & processes in their beverages. Easy to read FONT and preferably include an original picture of avocado (which can be a real picture / graphic design) - however, this is not necessary.

Company name: OWRU Pte.Ltd. (the letter "I" may mean "I" or "Innovative" or "Intelligent". "OWRU" can be a play of the word "I ever .... " e.g. "all OWRU wanted is ... ".)

Please note that the master label design should be versatile enough for a range of avocado smoothies (we only need to make minimum changes to the main picture / words as necessary for each specific avocado smoothie) and the label can also be used for kids size and adult size pouches and bottles of height 16cm and diameter of circular base of 5.5cm.

Target Market(s)

(1) health conscious busy professionals (e.g. gym / yoga / athletic buffs), (2) busy mothers of fussy / picky kids; and (3) vegans & people who like more plant based diets, who want the best products for them / their families.

Logo Text

OWRU

Font styles to use
Serif
Sans Serif
Decorative
Script

Colors

Designer to choose colors to be used in the design.

Requirements
Must have
• Centre attention of the label (BIG font): Avocado & [we insert the other main ingredients] Smoothie
• Company logo (noticeable somewhere on the label): OWRU
• (Medium font) All natural ingredients, no added sugar or salt, no additives or preservatives
• (Smaller fonts) Along the lines of: "Made from the finest blend of avocados and [we can insert other ingredients] to nourish you. Rich, creamy, wholesome & unique avocado experience that is good and satisfyingly delicious! "
• Keep refrigerated below 5 deg C
• Manufactured by: [we insert details]
• 300ml
Nice to have
• Please recycle usual logo
• originality & fresh & appealing factor
Should not have
• unhealthy image / junk food / sugary / additives / unsavoury impression
• difficult to read font
• confusion with other existing brands

```html
<!DOCTYPE html>
<html lang="en">
<head>
<meta charset="utf-8">
<title>OWRU Avocado Smoothie – Pouch Label</title>
<link rel="stylesheet" href="https://fonts.googleapis.com/css2?family=Oswald:wght@400;500;600&family=Yellowtail&family=Raleway:wght@400&family=Roboto+Condensed:wght@300&display=swap">
<style>
  :root {
    --page-bg: #e6e6e6;
    --lime-light: #9bdc2e;
    --lime: #7ccb22;
    --lime-deep: #63b41a;
    --leaf-dark: #2f5a18;
    --ink: #151515;
    --white: #ffffff;
    --logo-grey: #3a3f3a;
  }
  * { box-sizing: border-box; margin: 0; padding: 0; }
  html, body { width: 1200px; height: 960px; overflow: hidden; }
  body { background: var(--page-bg); position: relative; }

  .label {
    position: absolute;
    left: 420px; top: 110px;
    width: 360px; height: 740px;
    overflow: hidden;
  }
  .label__top {
    position: absolute; inset: 0 0 auto 0; height: 390px;
    background: linear-gradient(180deg, var(--lime-light), var(--lime));
    text-align: center;
  }
  .brand {
    position: absolute; top: 150px; left: 0; right: 0;
    display: flex; justify-content: center; align-items: center; gap: 10px;
    font-family: "Raleway", sans-serif; font-weight: 400;
    font-size: 44px; letter-spacing: 3px; color: var(--logo-grey);
  }
  .brand__dot { width: 12px; height: 12px; border-radius: 50%; background: var(--logo-grey); }
  .title {
    position: absolute; top: 228px; left: 0; right: 0;
    font-family: "Oswald", sans-serif; font-weight: 600;
    font-size: 70px; line-height: 1; color: var(--white); letter-spacing: -1px;
  }
  .subtitle {
    position: absolute; top: 294px; left: 0; right: 0;
    font-family: "Yellowtail", cursive; font-size: 60px; line-height: 1;
    color: var(--leaf-dark);
  }

  .label__bottom {
    position: absolute; left: 0; right: 0; top: 390px; bottom: 0;
    background: var(--ink);
  }
  .fruit-art {
    position: absolute; left: 22px; top: 22px; width: 300px; height: 160px;
    border-radius: 90px 120px 110px 80px / 80px 90px 90px 80px;
    background: linear-gradient(180deg, var(--lime-light), var(--lime));
  }
  .volume {
    position: absolute; right: 22px; top: 188px;
    font-family: "Oswald", sans-serif; font-weight: 400; font-size: 17px; line-height: 1.2;
    color: var(--white);
  }
  .claims {
    position: absolute; left: 0; right: 0; top: 220px;
    text-align: center;
    font-family: "Oswald", sans-serif; font-weight: 500;
    font-size: 15px; line-height: 1.05; color: var(--lime);
    text-transform: uppercase;
  }
  .blurb {
    position: absolute; left: 0; right: 0; bottom: 0; height: 58px;
    background: var(--lime-deep);
    padding: 9px 16px 0;
    text-align: center;
    font-family: "Roboto Condensed", sans-serif; font-weight: 300;
    font-size: 12px; line-height: 1.2; color: var(--ink);
  }
</style>
</head>
<body>
  <main class="label">
    <section class="label__top">
      <div class="brand"><span class="brand__name">OWRU</span><span class="brand__dot"></span></div>
      <h1 class="title">AVOCADO</h1>
      <p class="subtitle">smoothie</p>
    </section>
    <section class="label__bottom">
      <div class="fruit-art" role="img" aria-label="Stylised green avocado with leaf"></div>
      <p class="volume">300ml</p>
      <p class="claims">All natural ingredients,<br>no added sugar or salt,<br>no additives or preservatives</p>
      <p class="blurb">Made from the finest blend of avocados, to nourish you with a rich, creamy and unique avocado experience that is good and satisfyingly delicious!</p>
    </section>
  </main>
</body>
</html>
```